Ridgecrest Career Institute needs a unique tri-fold brochure design

I need a tri-fold brochure for my vocational school. We provide Nursing Assistant, Home Healthcare Aide & Phlebotomy classes at our centers and 50 programs online. The theme for our brochure and logo is Opening New Doors. I have all the text for the brochure and simples of brochures that I Like. I want the brochure to stand out and represent high quality and success. I also want the brochure to be easy to read. Yes, I'm also open to different ideas and concepts. lol
Updates

The logo and a sample of the text are now available with my brief.

Thanks,

Reg

Thanks to all the designers who took on the project and emailed me directly! If you have not replied to the invite, email me at, rmolvern47@quillpost.net

Thanks again, 
Reg 

Hello All,

Payment for the project is now GUARANTEED! Feel free to email me directly at rmolvern47@quillpost.net or you can post your first draft on my page. Fyi... full content for the brochure is only available upon request.

Thanks,

Reg

Target Market(s)

18-55 years old, but the vast majority are between the age of 24-45

Industry/Entity Type

School

Requirements
Must have
• Pictures of people in scrubs of all ages.
Should not have
• pictures of people in business wear.

```html
<!DOCTYPE html>
<html lang="en">
<head>
<meta charset="utf-8">
<title>Ridgecrest Career Institute – Tri-fold Brochure</title>
<link rel="stylesheet" href="https://fonts.googleapis.com/css2?family=Marcellus&family=Crimson+Text:wght@700&family=PT+Sans:wght@400;700&display=swap">
<style>
  :root {
    --ink-teal: #1f4a5a;
    --deep-teal: #1a3f4e;
    --band-teal: #3fa89c;
    --band-teal-light: #5ec0b3;
    --accent-orange: #e0582a;
    --panel-grey: #f2f2f2;
    --panel-grey-dark: #d9d9d9;
    --white: #ffffff;
    --body-text: #e6eef0;
  }
  * { margin: 0; padding: 0; box-sizing: border-box; }
  html, body { width: 1200px; height: 939px; overflow: hidden; background: var(--white); }
  .brochure { position: relative; width: 1200px; height: 939px; overflow: hidden; font-family: "PT Sans", sans-serif; }

  .inner-panel { position: absolute; left: 0; top: 0; width: 792px; height: 605px; background: var(--ink-teal); }
  .fold-accent { position: absolute; left: 792px; top: 0; width: 16px; height: 605px; background: var(--accent-orange); }
  .cover-panel { position: absolute; left: 808px; top: 0; width: 392px; height: 605px;
    background: linear-gradient(180deg, var(--white) 0%, var(--panel-grey) 55%, var(--panel-grey-dark) 100%); }

  .photo { position: absolute; }
  .photo-team { left: 26px; top: 26px; width: 383px; height: 256px;
    background: linear-gradient(180deg, #f4f5f7 0%, #dfe4ec 60%, #8fa6cf 100%); }
  .photo-student { left: 409px; top: 351px; width: 383px; height: 254px;
    background: linear-gradient(180deg, #e9e9e9 0%, #f6f6f6 55%, #b9cfe6 100%); }
  .photo-nurse { left: 875px; top: 301px; width: 210px; height: 304px;
    background: linear-gradient(180deg, rgba(220,220,220,0) 0%, #c7d2e6 45%, #2f5fa8 100%); }

  .section-title { position: absolute; color: var(--white); font-weight: 400; font-size: 31px; line-height: 1.1; }
  .section-body { position: absolute; color: var(--body-text); font-size: 12.5px; line-height: 20.4px; text-align: justify; }
  .training-title { left: 429px; top: 44px; }
  .training-body { left: 429px; top: 100px; width: 346px; }
  .education-title { left: 64px; top: 326px; }
  .education-body { left: 64px; top: 380px; width: 310px; }

  .headline { position: absolute; font-family: "Marcellus", serif; font-weight: 400; line-height: 0.95; letter-spacing: 1px; }
  .headline .line-dark { display: block; color: var(--ink-teal); }
  .headline .line-orange { display: block; color: var(--accent-orange); }
  .cover-headline { left: 808px; width: 392px; top: 22px; text-align: center; font-size: 54px; }
  .back-headline { left: 46px; top: 670px; font-size: 54px; }
  .back-headline .line-dark { color: #234e5e; }

  .benefits { position: absolute; left: 808px; width: 392px; top: 158px; list-style: none; text-align: center;
    font-family: "Crimson Text", serif; font-weight: 700; font-size: 16.5px; line-height: 28px; color: var(--ink-teal); }

  .back-band { position: absolute; left: 0; top: 605px; width: 1200px; height: 270px;
    background: linear-gradient(100deg, #2f9a8f 0%, var(--band-teal-light) 35%, var(--band-teal) 60%, #2c9488 100%); }
  .footer-strip { position: absolute; left: 0; top: 875px; width: 1200px; height: 64px; background: var(--deep-teal); }

  .contact { position: absolute; left: 435px; top: 656px; color: var(--white); font-style: normal; }
  .contact-name { font-size: 22px; font-weight: 400; margin-bottom: 4px; }
  .contact-line { font-size: 13px; line-height: 20.5px; }
  .contact-gap { height: 20px; }

  .call-to-action { position: absolute; left: 808px; width: 392px; top: 620px; text-align: center;
    font-family: "PT Sans", sans-serif; font-weight: 700; font-size: 21px; letter-spacing: 0.3px; color: var(--ink-teal); }
  .call-to-action .accent { color: var(--accent-orange); }

  .brand-mark { position: absolute; left: 808px; width: 392px; top: 690px; text-align: center; }
  .brand-square { display: block; width: 46px; height: 46px; margin: 0 auto 14px; background: var(--ink-teal); }
  .brand-name { font-family: "Crimson Text", serif; font-weight: 700; font-size: 28px; line-height: 30px; color: var(--ink-teal); }
</style>
</head>
<body>
<main class="brochure">
  <section class="inner-panel" aria-label="Inside panels"></section>
  <div class="fold-accent"></div>
  <section class="cover-panel" aria-label="Front cover"></section>

  <div class="photo photo-team" role="img" aria-label="Three smiling healthcare workers in blue scrubs"></div>
  <h2 class="section-title training-title">Fast &amp; Efficient Training</h2>
  <p class="section-body training-body">Maecenas accumsan lorem ut lacus tincidunt id pellentesque dolor porttitor. Etiam vel tellus sit amet risus tempor pellentesque in nec lorem. Ut ac lacus elit. Cras id sem dui. Nullam aliquam, leo non laoreet rutrum, velit nisl lobortis est, a semper libero lorem vel risus. Aliquam vulputate, tortor ac malesuada iaculis, magna diam tempor purus, vel aliquam erat leo non leo. Lorem ipsum dolor sit amet, consectetur adipiscing elit. Nemo enim ipsam voluptatem quia voluptas sit aspernatur aut odit aut fugit, sed quia consequuntur magni dolores eos qui ratione voluptatem sequi nesciunt.</p>

  <h2 class="section-title education-title">Affordable Education</h2>
  <p class="section-body education-body">Quisque ultrices elit et dui dignissim eu porttitor eros convallis. Donec imperdiet augue sit amet diam blandit dignissim. Suspendisse eu ante velit. Maecenas accumsan lorem ut lacus tincidunt id pellentesque dolor porttitor. Etiam vel tellus sit amet risus tempor pellentesque in nec lorem. Ut ac lacus elit. Cras id sem dui. Nullam aliquam, leo non laoreet rutrum, velit nisl lobortis est, a semper libero lorem vel risus. Aliquam vulputate, tortor ac malesuada iaculis, magna diam tempor purus, vel aliquam erat leo non leo.</p>
  <div class="photo photo-student" role="img" aria-label="Male nursing student in scrubs holding a clipboard"></div>

  <h1 class="headline cover-headline"><span class="line-dark">OPENING</span><span class="line-orange">NEW DOORS</span></h1>
  <ul class="benefits">
    <li>Affordable education &amp; Quality education</li>
    <li>Fast training &amp; Efficient training</li>
    <li>High paying jobs &amp; Rewarding careers</li>
    <li>State certified caregivers &amp; Highly rated employers</li>
    <li>Training facility &amp; Community</li>
  </ul>
  <div class="photo photo-nurse" role="img" aria-label="Smiling nurse in blue scrubs with a stethoscope, arms crossed"></div>

  <section class="back-band" aria-label="Back panels"></section>
  <div class="footer-strip"></div>

  <p class="headline back-headline"><span class="line-dark">OPENING</span><span class="line-orange">NEW DOORS</span></p>

  <address class="contact">
    <p class="contact-name">Ridgecrest Career Institute</p>
    <p class="contact-line">2010 Lorem Street, Ipsum Building</p>
    <p class="contact-line">Lorem City, UK</p>
    <div class="contact-gap"></div>
    <p class="contact-line">P. +00-0000-0000</p>
    <p class="contact-line">F. +00-0000-0000</p>
    <p class="contact-line">E. info@ridgecrestcareer.com</p>
    <p class="contact-line">W. www.ridgecrestcareer.com/aboutus</p>
  </address>

  <p class="call-to-action"><span class="accent">JOIN US</span> &amp; OPEN NEW <span class="accent">DOORS</span></p>
  <div class="brand-mark">
    <span class="brand-square"></span>
    <p class="brand-name">Ridgecrest<br>Career Institute</p>
  </div>
</main>
</body>
</html>
```